card design for engineering consultancy

engineering drafting and project management company the provides drafting services for.
Electrical, Hydraulic, Mechanical, and Civil services
The company is called K7R Services and logo is as attached
Information on card should be.
1. Logo
2.website : K7RServices.com
3. email : info@K7RServices.com
4. Phone: (+61) 400512738
5. Motto: Design - Document - Develop - Deliver

this card should be basically used for business identification only

Target Market(s)

electricians plumbers air conditioning installers and civil contractors

Industry/Entity Type

engineering, drafting, electrical, plumbing, airconditioning, civil

Contact Information for Business Card

1. Logo 2.website : K7RServices.com 3. email : info@K7RServices.com 4. Phone: (+61) 400512738 5. Motto: Design - Document - Develop - Deliver

Font styles to use
Serif

Requirements
Must have
• logo
Nice to have
• something inovative and different that makes it stand out from being just another business card

```html
<!DOCTYPE html>
<html lang="en">
<head>
<meta charset="utf-8">
<title>K7R Services – Business Card</title>
<link href="https://fonts.googleapis.com/css2?family=Montserrat:wght@400;500;600;700&display=swap" rel="stylesheet">
<style>
  :root {
    --canvas: #d9d9da;
    --charcoal: #4a4a4c;
    --ink: #444446;
    --red: #d0202e;
    --paper: #fafafa;
    --white: #ffffff;
  }
  * { margin: 0; padding: 0; box-sizing: border-box; }
  html, body { width: 1200px; height: 882px; overflow: hidden; }
  body {
    background: var(--canvas);
    font-family: "Montserrat", Arial, sans-serif;
    position: relative;
  }
  .card {
    position: absolute;
    left: 347px;
    width: 506px;
    height: 289px;
    box-shadow: 1px 2px 4px rgba(0,0,0,0.35);
  }
  .card--front { top: 129px; background: var(--charcoal); }
  .card--back  { top: 465px; background: var(--paper); }

  .brand-name {
    position: absolute;
    font-weight: 700;
    text-transform: uppercase;
    white-space: nowrap;
  }
  .card--front .brand-name {
    left: 0; right: 0;
    top: 118px;
    text-align: center;
    font-size: 36px;
    letter-spacing: 5px;
    color: var(--white);
  }
  .card--back .brand-name {
    right: 33px;
    top: 58px;
    font-size: 22px;
    letter-spacing: 3px;
    color: var(--charcoal);
  }

  .holder { position: absolute; left: 34px; top: 137px; }
  .holder-name {
    font-size: 23px;
    font-weight: 600;
    color: var(--ink);
    line-height: 1;
  }
  .holder-role {
    margin-top: 4px;
    font-size: 12px;
    font-weight: 500;
    color: var(--red);
  }

  .contact-list {
    position: absolute;
    left: 34px;
    top: 185px;
    list-style: none;
  }
  .contact-list li {
    display: flex;
    align-items: center;
    gap: 7px;
    height: 17px;
    font-size: 12.5px;
    color: var(--ink);
  }
  .contact-list svg { width: 11px; height: 11px; flex: none; }

  .motto {
    position: absolute;
    left: 34px;
    top: 249px;
    font-size: 12.5px;
    color: var(--ink);
  }
  .motto .dot { color: var(--red); margin: 0 3px; }
</style>
</head>
<body>
  <section class="card card--front">
    <div class="brand-name">K7R Services</div>
  </section>

  <section class="card card--back">
    <div class="brand-name">K7R Services</div>

    <div class="holder">
      <p class="holder-name">Marek Tolvan</p>
      <p class="holder-role">Executive Director</p>
    </div>

    <ul class="contact-list">
      <li>
        <svg viewBox="0 0 24 24" aria-hidden="true"><path fill="#d0202e" d="M6.6 10.8c1.4 2.8 3.8 5.1 6.6 6.6l2.2-2.2c.3-.3.7-.4 1-.2 1.1.4 2.3.6 3.6.6.6 0 1 .4 1 1V20c0 .6-.4 1-1 1C10.6 21 3 13.4 3 4c0-.6.4-1 1-1h3.5c.6 0 1 .4 1 1 0 1.3.2 2.5.6 3.6.1.3 0 .7-.2 1z"/></svg>
        (+61) 400512738
      </li>
      <li>
        <svg viewBox="0 0 24 24" aria-hidden="true"><rect x="2" y="5" width="20" height="14" fill="#d0202e"/><path d="M2 5l10 8 10-8" fill="none" stroke="#fafafa" stroke-width="2"/></svg>
        info@K7RServices.com
      </li>
      <li>
        <svg viewBox="0 0 24 24" aria-hidden="true"><g fill="none" stroke="#d0202e" stroke-width="2.2"><circle cx="12" cy="12" r="9.5"/><ellipse cx="12" cy="12" rx="4" ry="9.5"/><path d="M2.5 12h19M4 7h16M4 17h16"/></g></svg>
        www.K7RServices.com
      </li>
    </ul>

    <p class="motto">Design<span class="dot">•</span>Document<span class="dot">•</span>Develop<span class="dot">•</span>Deliver</p>
  </section>
</body>
</html>
```